Online medical reviews website needs banner advert!

We need banner advert templates for our website, www.traineepanel.net. These should meet the technical requirements of our partner (uploaded).

Our groundbreaking website allows doctors in training to rate and review their training.

The adverts should use the same modern design language and colour scheme as our website. They should use the text 'Help a junior doctor make a big decision - rate your training!'.

Vector assets should be supplied, allowing us to use alternative text in future.
Updates

Industry/Entity Type

Healthcare

Font styles to use
Other font styles liked:
• Karla

Colors
3277b5
0555a3
ffffff

Requirements
Must have
• Similar design to our website. Should be elegant & modern. Must allow future text to be easily inserted.
Should not have
• Unrelated design.

```html
<!DOCTYPE html>
<html lang="en">
<head>
<meta charset="utf-8">
<title>Trainee Panel – banner set</title>
<link rel="stylesheet" href="https://fonts.googleapis.com/css2?family=Arimo:wght@400;700&family=Roboto:wght@400;700&family=EB+Garamond:wght@400&display=swap">
<style>
  :root{
    --stage:#454344;
    --blue-light:#3277b5;
    --blue-deep:#0555a3;
    --white:#ffffff;
    --paper:#fbfbfc;
    --navy:#15308a;
  }
  html,body{margin:0;padding:0;overflow:hidden;background:var(--stage);}
  .stage{position:relative;width:1200px;height:1200px;background:var(--stage);overflow:hidden;}
  .banner{position:absolute;display:block;filter:drop-shadow(3px 3px 3px rgba(0,0,0,.45));}
  .banner--leaderboard{left:143px;top:250px;width:583px;height:72px;}
  .banner--square{left:273px;top:351px;width:349px;height:296px;}
  .banner--skyscraper{left:746px;top:193px;width:311px;height:612px;}
  .sans{font-family:"Roboto",Arial,sans-serif;}
  .sans-strong{font-family:"Arimo",Arial,sans-serif;font-weight:700;}
  .sans-plain{font-family:"Arimo",Arial,sans-serif;font-weight:400;}
  .serif{font-family:"EB Garamond",Garamond,serif;}
</style>
</head>
<body>
<main class="stage">

  <!-- Leaderboard -->
  <svg class="banner banner--leaderboard" viewBox="0 0 583 72" aria-label="Leaderboard banner">
    <rect width="583" height="72" fill="var(--white)"/>
    <polygon points="413,0 583,0 583,72 410,72 449,36" fill="var(--blue-deep)"/>
    <text class="sans" x="22" y="44" font-size="21" fill="var(--blue-light)">Help a junior doctor make a big decision</text>
    <text class="sans-strong" x="512" y="33" font-size="16" fill="var(--white)" text-anchor="middle" letter-spacing="0.6">rate your</text>
    <text class="sans-strong" x="512" y="53" font-size="16" fill="var(--white)" text-anchor="middle" letter-spacing="0.6">training!</text>
  </svg>

  <!-- Square -->
  <svg class="banner banner--square" viewBox="0 0 349 296" aria-label="Square banner">
    <rect width="349" height="296" fill="var(--paper)"/>
    <polygon points="0,0 349,0 349,183 199,183 169,213 139,183 0,183" fill="var(--blue-light)"/>
    <text class="serif" x="174" y="75" font-size="35" fill="var(--white)" text-anchor="middle">Help a junior doctor</text>
    <text class="serif" x="174" y="121" fill="var(--white)" text-anchor="middle"><tspan font-size="32">make a big </tspan><tspan font-size="46">decision</tspan></text>
    <text class="sans-strong" x="179" y="265" font-size="26" fill="var(--blue-light)" text-anchor="middle" style="font-family:'Roboto',Arial,sans-serif">Rate Your Training!</text>
  </svg>

  <!-- Skyscraper -->
  <svg class="banner banner--skyscraper" viewBox="0 0 311 612" aria-label="Skyscraper banner">
    <rect width="311" height="612" fill="var(--white)"/>
    <rect width="311" height="439" fill="var(--blue-deep)"/>
    <polygon points="0,439 146,439 146,539 0,451" fill="var(--blue-light)"/>
    <polygon points="146,439 311,439 146,539" fill="var(--blue-deep)"/>
    <text class="sans-plain" x="22" y="89" font-size="72" fill="var(--white)">Help</text>
    <text class="sans-plain" x="23" y="141" font-size="38" fill="var(--white)">a junior doctor</text>
    <text class="sans-plain" x="24" y="191" font-size="38" fill="var(--white)">make a big</text>
    <text class="sans-strong" x="24" y="244" font-size="48" fill="var(--white)">decision</text>
    <text class="sans-strong" x="31" y="383" font-size="22" fill="var(--white)" letter-spacing="0.4">- rate your training!</text>
    <g class="brand" aria-label="Trainee Panel">
      <text class="sans-plain" x="6" y="586" font-size="35" fill="var(--navy)" letter-spacing="-0.5">Trainee Panel</text>
      <rect x="262" y="560" width="20" height="20" fill="var(--navy)"/>
    </g>
  </svg>

</main>
</body>
</html>
```